Psychology practice - information brochure/flyer - half A4 page folded (4 sides)

We need a brochure/flyer to market our psychology service to GPs (Doctors). We need to demonstrate to the doctors that we are the right choice for their patients, and that we cover a large range of services so all of their patients needs are met. We will demonstrate this by listing our range of services and our team of psychologists. We have two locations in Sydney and offer high end services. I've attached our company logo but we remain flexible regarding the style of the brochures. I will provide more details (services, locations & psychologist credentials) once our preferred brochure design has been selected.

```html
<!DOCTYPE html>
<html lang="en">
<head>
<meta charset="utf-8">
<title>Bright Mind Clinical Psychology – Brochure Spread</title>
<link href="https://fonts.googleapis.com/css2?family=Open+Sans:wght@400;600;700&family=Josefin+Sans:wght@300&display=swap" rel="stylesheet">
<style>
  :root {
    --backdrop: #d4d4d6;
    --cream: #f4ead2;
    --gold: #d8b42c;
    --gold-soft: rgba(222, 186, 48, 0.92);
    --header-text: #f7eaa6;
    --panel: rgba(78, 78, 80, 0.88);
    --panel-text: #e6e6e6;
    --heading-dark: #6e6a62;
    --body-muted: #8f8a80;
    --client-text: #7a6a2a;
    --white: #ffffff;
  }
  * { box-sizing: border-box; margin: 0; padding: 0; }
  html, body { width: 1200px; height: 900px; overflow: hidden; }
  body {
    background: var(--backdrop);
    font-family: "Open Sans", sans-serif;
    position: relative;
  }
  .spread {
    position: absolute; left: 50px; top: 56px;
    width: 1100px; height: 788px;
    display: flex;
  }
  .page { position: relative; width: 550px; height: 788px; overflow: hidden; }

  /* Left page */
  .page-left .photo {
    position: absolute; inset: 0;
    background:
      radial-gradient(ellipse 70% 35% at 45% 72%, rgba(255, 214, 140, 0.9), rgba(255,214,140,0) 70%),
      linear-gradient(180deg, #f5ecd5 0%, #f3e5c4 38%, #e9c98f 58%, #cf9a64 76%, #6b4a55 100%);
  }
  .clinicians { position: absolute; left: 36px; top: 34px; width: 222px; }
  .clinicians h2 {
    font-size: 15px; font-weight: 600; color: var(--heading-dark);
    padding-bottom: 3px; border-bottom: 1px solid var(--gold);
    margin-bottom: 30px;
  }
  .clinician { font-size: 12.5px; line-height: 14.6px; color: var(--body-muted); margin-bottom: 14px; }
  .clinician strong { display: block; color: var(--heading-dark); font-weight: 600; }

  .fee-box { position: absolute; left: 295px; top: 36px; width: 222px; }
  .box-header {
    background: var(--gold); color: var(--header-text);
    font-size: 14.5px; font-weight: 600; text-transform: uppercase;
    height: 36px; line-height: 36px; padding-left: 17px;
  }
  .box-body {
    background: var(--panel); color: var(--panel-text);
    font-size: 12.5px; line-height: 14.6px; padding: 13px 12px 14px 17px;
  }
  .fee-group + .fee-group { margin-top: 14px; }
  .fee-group h3 { font-size: 12.5px; font-weight: 700; text-transform: uppercase; }
  .fee-group .sub { font-weight: 700; }
  ul.bullets { list-style: none; }
  ul.bullets li { position: relative; padding-left: 12px; }
  ul.bullets li::before { content: "•"; position: absolute; left: 1px; }

  .brand {
    position: absolute; left: 318px; top: 692px;
    color: var(--white); font-family: "Josefin Sans", sans-serif; font-weight: 300;
    font-size: 27px; line-height: 30px;
    display: flex; align-items: center; gap: 10px;
  }
  .brand-mark { width: 22px; height: 22px; border-radius: 50%; background: var(--white); flex: none; }

  /* Right page */
  .page-right .photo {
    position: absolute; inset: 0;
    background:
      radial-gradient(circle at 115% 62%, #2a2214 0 18%, rgba(42,34,20,0) 28%),
      radial-gradient(ellipse 80% 60% at 80% 55%, #f2c21c, rgba(242,194,28,0) 75%),
      linear-gradient(160deg, #e8d77a 0%, #d9b63a 35%, #b98d1a 60%, #6e5a2a 100%);
  }
  .services-box { position: absolute; left: 42px; top: 36px; width: 471px; }
  .services-box .box-body { display: flex; gap: 0; padding: 13px 10px 14px 14px; }
  .services-box ul.bullets { width: 50%; }
  .services-box ul.bullets:first-child { width: 48%; }

  .clients-box {
    position: absolute; left: 42px; top: 333px; width: 256px; height: 180px;
    background: var(--gold-soft); padding: 14px 12px 0 16px;
    font-size: 12.5px; line-height: 14.6px; color: var(--client-text);
  }
  .clients-box h3 { font-size: 12.5px; font-weight: 600; color: #5e5230; }

  .hours { position: absolute; left: 0; bottom: 0; width: 240px; height: 170px; }
  .hours svg { position: absolute; left: 0; top: 0; }
  .hours-text {
    position: absolute; left: 36px; top: 46px;
    color: var(--white); font-size: 12.5px; line-height: 14.6px;
  }
  .hours-text h3 { font-size: 12.5px; font-weight: 600; text-transform: uppercase; }
  .hours-text .day { font-weight: 700; }

  .fold {
    position: absolute; left: 530px; top: 0; width: 40px; height: 788px;
    background: linear-gradient(90deg, rgba(0,0,0,0) 0%, rgba(0,0,0,0.14) 50%, rgba(0,0,0,0) 100%);
    pointer-events: none;
  }
</style>
</head>
<body>
  <main class="spread">
    <section class="page page-left">
      <div class="photo" role="img" aria-label="Sunset photograph of a woman with outstretched arms facing the sky, in warm golden light"></div>

      <div class="clinicians">
        <h2>Our Clinicians</h2>
        <p class="clinician"><strong>Dr Helena Marsh</strong>D ClinPsych, MA, BSc (Psych),<br>BPsych (Hons)</p>
        <p class="clinician"><strong>Dr Thomas Edward Lyle</strong>DPhil (Psych), BA-Psych (Hons),<br>GradDipEd, GDipMgt, MAPS, FCOP</p>
        <p class="clinician"><strong>Linda Carroway</strong>MPsych (Clin), BPsych (Hons)</p>
        <p class="clinician"><strong>Priya Nandan</strong>BPsych (Hons), GDipPsych</p>
        <p class="clinician"><strong>Dr Sofia Renard</strong>D ClinPsych, MSc (Psych),<br>B Psych (Hons), MACPA, MAPS</p>
      </div>

      <div class="fee-box">
        <div class="box-header">Our Fee Structure</div>
        <div class="box-body">
          <div class="fee-group">
            <h3>Business Hours</h3>
            <p class="sub">9am to 5pm</p>
            <ul class="bullets">
              <li>$150 per session for General Psychologist, with Medicare Rebate of $84.80</li>
              <li>$190 per session for Clinical Psychologist, with Medicare Rebate of $124.50</li>
            </ul>
          </div>
          <div class="fee-group">
            <h3>Out of Hours</h3>
            <p class="sub">weekends and after 5pm</p>
            <ul class="bullets">
              <li>$170 per session for General Psychologist, with Medicare Rebate of $84.80</li>
              <li>$210 per session for Clinical Psychologist, with Medicare Rebate of $124.50</li>
            </ul>
          </div>
        </div>
      </div>

      <div class="brand">
        <span class="brand-mark"></span>
        <span>Bright Mind<br>Clinical Psychology</span>
      </div>
    </section>

    <section class="page page-right">
      <div class="photo" role="img" aria-label="Close-up photograph of a bright yellow sunflower with a dark seed centre"></div>

      <div class="services-box">
        <div class="box-header">Type of Services We Provide</div>
        <div class="box-body">
          <ul class="bullets">
            <li>Anxiety</li>
            <li>Depression</li>
            <li>Attention Deficit Hyperactivity Disorder (ADHD)</li>
            <li>Phobias</li>
            <li>Autism Spectrum Disorder</li>
            <li>Intellectual disability</li>
            <li>Learning difficulties</li>
            <li>Bullying</li>
            <li>Study stress</li>
            <li>Procrastination</li>
            <li>WorkCover</li>
            <li>Stress management</li>
          </ul>
          <ul class="bullets">
            <li>Rehabilitation psychology</li>
            <li>Addiction and relapse prevention</li>
            <li>Anger management</li>
            <li>Divorce/separation</li>
            <li>Pregnancy</li>
            <li>Trauma</li>
            <li>Post-Traumatic Stress Disorder (PTSD)</li>
            <li>Couples/Family Therapy</li>
            <li>Domestic Violence</li>
            <li>Non-Suicidal Self Injury</li>
            <li>Grief and loss</li>
            <li>Eating disorders / body image</li>
          </ul>
        </div>
      </div>

      <div class="clients-box">
        <h3>Our Client Groups</h3>
        <ul class="bullets">
          <li>Children 5-12</li>
          <li>Adolescents</li>
          <li>Adults</li>
          <li>Veterans</li>
          <li>Victims of crime</li>
          <li>Injured workers</li>
          <li>Culturally and Linguistically Diverse backgrounds</li>
          <li>Refugees</li>
        </ul>
      </div>

      <div class="hours">
        <svg width="240" height="170" viewBox="0 0 240 170" aria-hidden="true">
          <path d="M0 30 Q100 -10 170 30 Q240 80 230 170 L0 170 Z" fill="rgba(70,66,58,0.55)"/>
          <path d="M0 30 Q100 -10 170 30 Q240 80 230 170" fill="none" stroke="#e6b82a" stroke-width="1.5"/>
        </svg>
        <div class="hours-text">
          <h3>Hours of Operation</h3>
          <p class="day">Monday – Friday</p>
          <p>8am-6pm</p>
          <p class="day">Saturday</p>
          <p>9am – 1pm</p>
        </div>
      </div>
    </section>

    <div class="fold" aria-hidden="true"></div>
  </main>
</body>
</html>
```